Buchcover-Design für Fachbuch
Tolle Entwürfe und ein sehr effiziente Zusammenarbeit. Können wir nur weiterempfehlen.
Zielgruppe
Unternehmensberatung im Thema Arbeitszeit. Wir haben ein Fachbuch zum Thema Arbeitszeit und Personaleinsatzplanung für Geschäftsführer, HR Mitarbeiter, Führungskräfte, Studenten und alle geschrieben, die sich o.g. Themen näher informieren möchten
Aufgabenstellung
Folgende Textelemente sollen zu sehen sein:
Autorennamen: Dr. Reinhold Kattner, Lothar Brenning
Titel: PLAN STARK Betrieb - Dienstzeiten und Schichtorganisation fair, rentabel und marktnah einrichten
Außerdem: Unter Mitwirkung von Prof. Anton K. Ruhland
Und: mit vielen Praxisbeispielen (ggf. als eine Art Plakette)
Auf der Rückseite soll ein Klappentext und 2 Zitate zu sehen sein:
Klappentext:
Die Welt verändert sich dramatisch. Digitalisierung, Fachkräftemangel, Wertewandel und nicht zuletzt Ausnahmezustände wie die Coronakrise stellen Unternehmen vor große Herausforderungen. Wie können Unternehmen flexibel und gleichzeitig wirtschaftlich, kunden- und mitarbeiterorientiert agieren?
Reinhold Kattner und Lothar Brenning sehen eine innovative Arbeitszeitgestaltung als entscheidenden Hebel an, um Unternehmen aller Branchen in schnelllebigen Märkten flexibel aufzustellen. Die Autoren beleuchten mit vielen Beispielen aus ihrer Beratungspraxis, warum Arbeitszeitsysteme dringend modernisiert werden müssen und welche Möglichkeiten Sie bereits heute haben, Arbeitszeit innovativ zu gestalten.
Sie erfahren alles Wissenswerte über klassische Modelle, wie z.B. Schichtplan, Gleitzeit, Vertrauensarbeitszeit, Zeitkontensystem und Teilzeit, über Workforce Management (Workforce Analytics, Personalbedarfsermittlung und Forecast, Personaleinsatzplanung, Zeiterfassung) bis hin zu Lebensarbeitszeit, Gruppenarbeit, Selbstorganisation, Homeoffice und New Work. Dabei lernen Sie nicht nur die Einzelkomponenten kennen, sondern erfahren auch, wie man diese geschickt zu einer für Mitarbeiter und Unternehmen gleichermaßen vorteilhaften Arbeitszeitsystematik kombiniert. Neben diesem strategischen Wissen vermitteln Ihnen die Autoren hilfreiche Methoden zur konkreten operativen Umsetzung dieser Themen.
Zitat 1:
„Durch die Weitergabe ihrer umfassenden Erfahrungen aus der Beratung ist es den Autoren in hervorragender Weise gelu..

```html
<!DOCTYPE html>
<html lang="de">
<head>
<meta charset="utf-8">
<title>Buchrückseite – PLAN STARK Betrieb</title>
<link href="https://fonts.googleapis.com/css2?family=Roboto:wght@400;700&display=swap" rel="stylesheet">
<style>
  :root {
    --green: #9bcd32;
    --navy: #003a70;
    --lavender: #c8cde1;
    --white: #ffffff;
    --frame: #9a9a9a;
  }
  * { margin: 0; padding: 0; box-sizing: border-box; }
  html, body {
    width: 848px; height: 1200px; overflow: hidden;
    background: var(--white);
    font-family: "Roboto", Arial, sans-serif;
  }
  .back-cover {
    position: absolute; left: 81px; top: 190px;
    width: 686px; height: 889px;
    border: 1px solid var(--frame);
    overflow: hidden;
  }
  .photo-area {
    position: absolute; left: 0; top: 0; width: 229px; height: 202px;
    background: linear-gradient(135deg, #f4f4f2 0%, #e6e2dc 45%, #cfd3d6 100%);
  }
  .quote-top {
    position: absolute; left: 229px; top: 0; width: 457px; height: 202px;
    background: var(--green); color: var(--white);
    padding: 14px 30px 0 23px;
    font-size: 13.7px; line-height: 20px;
  }
  .quote-top .source { margin-top: 12px; }
  .quote-top strong { font-weight: 700; }
  .side-strip {
    position: absolute; left: 0; top: 202px; width: 20px; height: 687px;
    background: var(--green);
  }
  .blurb {
    position: absolute; left: 20px; top: 202px; width: 666px; height: 484px;
    background: var(--navy); color: var(--white);
    padding: 24px 30px 0 21px;
    font-size: 13.7px; line-height: 21.3px;
    hyphens: auto;
  }
  .blurb p + p { margin-top: 21.3px; }
  .quote-bottom {
    position: absolute; left: 20px; top: 686px; width: 418px; height: 203px;
    background: var(--white); color: var(--navy);
    padding: 12px 0 0 21px;
    font-size: 13.7px; line-height: 20px;
  }
  .quote-bottom .source { margin-top: 14px; }
  .isbn-panel {
    position: absolute; left: 438px; top: 686px; width: 248px; height: 203px;
    background: var(--lavender);
  }
  .isbn-label {
    position: absolute; left: 17px; top: 60px;
    color: var(--white); font-size: 11.5px;
  }
  .isbn-field {
    position: absolute; left: 17px; top: 79px; width: 199px; height: 93px;
    background: var(--white);
  }
</style>
</head>
<body>
  <div class="back-cover">
    <div class="photo-area" role="img" aria-label="Foto: lächelnde Mitarbeiterin mit Brille am Laptop in einem hellen Büro"></div>

    <div class="quote-top">
      <p>„Durch die Weitergabe ihrer umfassenden Erfahrungen aus der Beratung ist es den Autoren in hervorragender Weise gelungen, neue Einsichten und vertieftes Expertenwissen sowohl zur Implementierung von New Workforce Management-Lösungen als auch zu konkreten Vorgehensweisen bei der Personaleinsatzplanung zu vermitteln.“</p>
      <p class="source"><strong>Anton K. Ruhland,</strong><br>Professor für Personalmanagement an der HSW Merzburg</p>
    </div>

    <div class="side-strip"></div>

    <div class="blurb">
      <p>Die Welt verändert sich dramatisch. Digitalisierung, Fachkräftemangel, Wertewandel und nicht zuletzt Ausnahmezustände wie die Coronakrise stellen Unternehmen vor große Herausforderungen. Wie können Unternehmen flexibel und gleichzeitig wirtschaftlich, kunden- und mitarbeiterorientiert agieren?</p>
      <p>Reinhold Kattner und Lothar Brenning sehen eine innovative Arbeitszeitgestaltung als entscheidenden Hebel an, um Unternehmen aller Branchen in schnelllebigen Märkten flexibel aufzustellen. Die Autoren beleuchten mit vielen Beispielen aus ihrer Beratungspraxis, warum Arbeitszeitsysteme dringend modernisiert werden müssen und welche Möglichkeiten Sie bereits heute haben, Arbeitszeit innovativ zu gestalten.</p>
      <p>Sie erfahren alles Wissenswerte über klassische Modelle, wie z.B. Schichtplan, Gleitzeit, Vertrauensarbeitszeit, Zeitkontensystem und Teilzeit, über Workforce Management (Workforce Analytics, Personalbedarfsermittlung und Forecast, Personaleinsatzplanung, Zeiterfassung) bis hin zu Lebensarbeitszeit, Gruppenarbeit, Selbstorganisation, Homeoffice und New Work. Dabei lernen Sie nicht nur die Einzelkomponenten kennen, sondern erfahren auch, wie man diese geschickt zu einer für Mitarbeiter und Unternehmen gleichermaßen vorteilhaften Arbeitszeitsystematik kombiniert. Neben diesem strategischen Wissen vermitteln Ihnen die Autoren hilfreiche Methoden zur konkreten operativen Umsetzung dieser Themen.</p>
    </div>

    <div class="quote-bottom">
      <p>„Das vorliegende Buch von Kattner und Brenning liefert den entscheidenden Baustein zur Humanisierung von Ökonomie und Unternehmensorganisation und hat das Potenzial zu dem Standardwerk im Thema moderne Arbeitszeitgestaltung und Workforce Management zu werden.“</p>
      <p class="source"><strong>Dr. Ulrich Brandeis,</strong> Initiator des Kompetenznetzwerks Fachforum Kompass &amp; Top 3 HR Influencer 2020 (Arbeitswelt Journal)</p>
    </div>

    <div class="isbn-panel">
      <span class="isbn-label">ISBN-Nr.:</span>
      <div class="isbn-field"></div>
    </div>
  </div>
</body>
</html>
```